Norwegian psychologist service needs a fresh and exiting web site*

Norwegian psychologist service: working with therapy, personal development, mastery and personal growth. Focus: children and teenagers with special needs; family dynamics; group processes; individuals with a need for therapy and personal growth. (Our company name: Kildeløft og ro (means Mastery and Growth).

We already have a logo for the company, which will be used (will be attached in the project).

The webside is to be structured in 4 pages with roll down curtain menus (the numbers are just for guiding the designer - the should not be added):

Page 1: Om Kildeløft og Ro (about Mastery and Growth): this is where our business is is presented/described shortly: Lorem Ipsum dolor cit...

Page 2: Tjenester (Services): this is where our 5 service areas are presented:
2.1 Utredning (Investigation, diagnosing): Lorem Ipsum dolor cit...
2.2 Rådgivning (consulting): Lorem Ipsum dolor cit...

2.3 Kurs og work shops (courses and work shops): Lorem Ipsum dolor cit...
2.3a Kildeløft og ro Tema 1 (T1)
2.3b Kildeløft og ro Tema 2 (T2)
2.3c Kildeløft og ro Tema 3 (T3)

2.4 Terapi og utvikling (Therapy and development)
2.4a Kildeløft og ro for individer (KR1)
2.4b Kildeløft og ro i familier (KR2)
2.4c Kildeløft og ro i grupper (KR3)
2.4d Kildeløft og ro i institusjoner (KR4)

Page 3: Aktuelt (Blog): this is our blog where we share knowledge and articles

Page 4: Kontakt (Contact): This is the contact form page. Contact form should constitute:
- Ditt navn (your name)
- E-post (your e-mail)
- Emne (subject)
- Melding (message/description)

Our project should also include suggestion for handheld units (iPhone, iPad).
Updates

We have both been traveling with work for a while, and then unfortunately both of us got sick on return, so we need a few more days to evaluate and choose design. Kind Regards Arne & Ragnhild

Target Market(s)

Focus on therapy, learning, mastery and growth for children and teenagers with special needs, within the family dynamics, or in a group setting.
OUR MARKETS:
Private market: individuals, families, groups and health industry institutions (with focus on learning, mastery, growth (as well as growing up) and psychiatry for children and teenagers with special difficulties and needs)
Public institutions: Government institutions, state institutions and municipality institutions (e.g. schools, municipality health service, hospitals) that serve the public (families with children and teenagers with special needs, and where learning, mastery, growth (as well as growing up) and potential psychiatry is an issue).

Number of Pages Required

4 page

Font styles to use
Sans Serif

Colors

Designer to choose colors to be used in the design.

Requirements
Must have
• The website must have 4 pages with roll down curtain menus (we have added a PDF with suggested structure, and headings, with sub menus - see attached PDF drawing.
• The web page must also use the added logo file - and make the web page work well with our logo.
• We would like the website to have a modern look and we would like the site to be associated with typical HIGH END TOP QUALITY private health institutions, but with a stronger focus on human beings (hands, faces etc), and not white coats and doctors. We are psychologists in the private market.
• For instance, if photos are being used - we tend to like "warm" almost art-like, "grainy" two-tone (e.g. sepia) photos to illustrate our focus. If designer can find such photos as part of design, it would be interesting to us. We would like a few photos like that integrated in the design.
• We also want a design suggestion for how the web page should look like and behave on handheld units (e.g. iPhone, iPad).
Nice to have
• If designer could find a number of suitable photos that matches the business idea and design requirements (see description above), that could follow website, that would be good.
• It could also be nice to have graphic symbols that denote the different pages/subpages (subjects)....
• HORSES: we sometimes use horses as a "tool" in therapy sessions. The horse is not necessarily used for riding, but for contact, communication and grooming. PHOTOS: we would like the designer to find an opportunity for using a photo reflecting this cooperation between therapist, child, teenager and horse. It is a bit up to the designer to find a way to do this... Since the horse is only a tool, among many other tools, it does not have to be much - but we want to try and see how it will work with a photo that also reflects this part of our business.

```html
<!DOCTYPE html>
<html lang="no">
<head>
<meta charset="utf-8">
<title>Kildeløft og Ro – Tjenester</title>
<link rel="stylesheet" href="https://fonts.googleapis.com/css2?family=Source+Sans+3:wght@300;400;600&display=swap">
<style>
  :root {
    --backdrop-top: #2a4a60;
    --backdrop-bottom: #e3e5e6;
    --white: #ffffff;
    --brand-blue: #2b3a96;
    --teal: #2b4d63;
    --charcoal: #232323;
    --strip: #1c1c1c;
    --light-text: #e9eef1;
    --icon: #f2f2f2;
    --plus-bg: #f4f4f4;
    --plus-fg: #2a2a2a;
  }
  * { box-sizing: border-box; margin: 0; padding: 0; }
  html, body {
    width: 1200px; height: 1023px; overflow: hidden;
    background: var(--backdrop-bottom);
    font-family: "Source Sans 3", "Segoe UI", sans-serif;
  }
  .backdrop-band {
    position: absolute; left: 0; top: 0; width: 1200px; height: 508px;
    background: var(--backdrop-top);
  }
  .site {
    position: absolute; left: 177px; top: 79px;
    width: 873px; height: 816px; overflow: hidden;
    background: var(--white);
    box-shadow: 0 14px 30px rgba(0,0,0,0.18);
  }
  .site-header {
    position: absolute; left: 0; top: 0; width: 100%; height: 77px;
    background: var(--white);
  }
  .brand {
    position: absolute; left: 172px; top: 8px; width: 90px;
    display: flex; flex-direction: column; align-items: center; gap: 4px;
  }
  .brand-dot { width: 30px; height: 30px; border-radius: 50%; background: var(--brand-blue); }
  .brand-name {
    font-size: 13px; font-weight: 600; color: var(--brand-blue);
    white-space: nowrap; line-height: 1;
  }
  .main-nav {
    position: absolute; left: 279px; top: 29px;
    font-size: 15px; color: var(--brand-blue); white-space: nowrap;
  }
  .main-nav a { color: inherit; text-decoration: none; }
  .main-nav .sep { margin: 0 7px; }

  .hero {
    position: absolute; left: 0; top: 77px; width: 100%; height: 377px;
    background:
      radial-gradient(ellipse 60% 70% at 45% 55%, rgba(196,186,168,0.55), rgba(0,0,0,0) 70%),
      linear-gradient(180deg, #b7ad99 0%, #8a8272 30%, #4f4a42 70%, #2e2c28 100%);
  }
  .hero-arrow { position: absolute; top: 165px; width: 20px; height: 32px; }
  .hero-arrow.prev { left: 2px; }
  .hero-arrow.next { right: 2px; }

  .section-band {
    position: absolute; left: 0; top: 454px; width: 100%; height: 26px;
    background: var(--teal);
  }
  .section-title {
    position: absolute; left: 0; top: 439px; width: 100%;
    padding-left: 30px;
    text-align: center; font-weight: 300; font-size: 38px; line-height: 1;
    color: var(--light-text); letter-spacing: 0.5px;
  }

  .services { position: absolute; left: 0; top: 480px; width: 100%; height: 336px; }
  .services-strip { position: absolute; left: 0; top: 0; width: 44px; height: 100%; background: var(--strip); }
  .service {
    position: absolute; left: 44px; width: 461px; height: 112px;
    color: var(--light-text);
  }
  .service.teal { background: var(--teal); }
  .service.dark { background: var(--charcoal); }
  .service:nth-of-type(1) { top: 0; }
  .service:nth-of-type(2) { top: 112px; }
  .service:nth-of-type(3) { top: 224px; }
  .service-icon { position: absolute; left: 18px; top: 20px; width: 70px; height: 70px; }
  .service-title { position: absolute; left: 105px; top: 14px; font-size: 15px; font-weight: 400; }
  .service-text {
    position: absolute; left: 105px; top: 38px; width: 312px;
    font-size: 12.5px; line-height: 15px; font-weight: 300;
  }
  .service-more {
    position: absolute; right: -14px; top: 40px; width: 28px; height: 28px;
    z-index: 2;
  }
  .services-photo {
    position: absolute; left: 505px; top: 0; width: 368px; height: 100%;
    background:
      linear-gradient(90deg, rgba(70,90,50,0.35) 0%, rgba(70,90,50,0) 12%),
      linear-gradient(170deg, #ddd3cd 0%, #cbbab2 45%, #a8968a 75%, #6f6257 100%);
  }
</style>
</head>
<body>
  <div class="backdrop-band"></div>
  <main class="site">
    <header class="site-header">
      <div class="brand">
        <span class="brand-dot"></span>
        <span class="brand-name">Kildeløft og Ro</span>
      </div>
      <nav class="main-nav">
        <a href="#">Om Kildeløft og Ro</a><span class="sep">|</span><a href="#">Tjenester</a><span class="sep">|</span><a href="#">Aktuelt</a><span class="sep">|</span><a href="#">Kontakt</a>
      </nav>
    </header>

    <section class="hero" role="img" aria-label="Sepia photo of five colleagues talking and laughing in a relaxed lounge">
      <svg class="hero-arrow prev" viewBox="0 0 20 32"><polyline points="15,4 4,16 15,28" fill="none" stroke="#fff" stroke-width="2"/></svg>
      <svg class="hero-arrow next" viewBox="0 0 20 32"><polyline points="5,4 16,16 5,28" fill="none" stroke="#fff" stroke-width="2"/></svg>
    </section>

    <div class="section-band"></div>
    <h2 class="section-title">TJENESTER</h2>

    <section class="services">
      <div class="services-strip"></div>

      <article class="service teal">
        <svg class="service-icon" viewBox="0 0 70 70" fill="none" stroke="var(--icon)" stroke-width="2.5">
          <rect x="4" y="6" width="52" height="40"/>
          <polyline points="10,36 20,22 30,30 44,14"/>
          <circle cx="42" cy="42" r="11" fill="var(--teal)"/>
          <line x1="50" y1="50" x2="64" y2="64" stroke-width="5"/>
        </svg>
        <h3 class="service-title">Utredning</h3>
        <p class="service-text">Lorem ipsum dolor sit amet, consectetuer adipiscing elit, sed diam nonummy nibh euismod tincidunt ut laoreet dolore magna</p>
        <svg class="service-more" viewBox="0 0 28 28"><circle cx="14" cy="14" r="13" fill="var(--plus-bg)"/><path d="M14 7v14M7 14h14" stroke="var(--plus-fg)" stroke-width="2.5"/></svg>
      </article>

      <article class="service dark">
        <svg class="service-icon" viewBox="0 0 70 70" fill="var(--icon)">
          <path d="M22 4h44v28H44l-8 8v-8H22z" fill="none" stroke="var(--icon)" stroke-width="2.5"/>
          <circle cx="30" cy="10" r="2"/><circle cx="36" cy="10" r="2"/><circle cx="42" cy="10" r="2"/>
          <circle cx="20" cy="38" r="10"/>
          <path d="M2 68c0-13 8-20 18-20s18 7 18 20z"/>
        </svg>
        <h3 class="service-title">Rådgivning</h3>
        <p class="service-text">Lorem ipsum dolor sit amet, consectetuer adipiscing elit, sed diam nonummy nibh euismod tincidunt ut laoreet dolore magna</p>
        <svg class="service-more" viewBox="0 0 28 28"><circle cx="14" cy="14" r="13" fill="var(--plus-bg)"/><path d="M14 7v14M7 14h14" stroke="var(--plus-fg)" stroke-width="2.5"/></svg>
      </article>

      <article class="service teal">
        <svg class="service-icon" viewBox="0 0 70 70" fill="var(--icon)">
          <circle cx="14" cy="28" r="7"/><path d="M2 54c0-9 5-15 12-15s12 6 12 15z"/>
          <circle cx="56" cy="28" r="7"/><path d="M44 54c0-9 5-15 12-15s12 6 12 15z"/>
          <circle cx="35" cy="24" r="9"/><path d="M20 56c0-11 6-18 15-18s15 7 15 18z"/>
        </svg>
        <h3 class="service-title">Kurs og work shops</h3>
        <p class="service-text">Lorem ipsum dolor sit amet, consectetuer adipiscing elit, sed diam nonummy nibh euismod tincidunt ut laoreet dolore magna</p>
        <svg class="service-more" viewBox="0 0 28 28"><circle cx="14" cy="14" r="13" fill="var(--plus-bg)"/><path d="M14 7v14M7 14h14" stroke="var(--plus-fg)" stroke-width="2.5"/></svg>
      </article>

      <div class="services-photo" role="img" aria-label="Warm-toned photo of a small group relaxing on a sofa in a bright room with a tall window and climbing plants"></div>
    </section>
  </main>
</body>
</html>
```